Pricing Poster selling novelty toys and snacks at a Halloween event

I need a poster made for our Halloween event. It would incorporate the items offered and pricing for each.

selling novelty toys and snacks

The Poster needs to say :
PRICE LIST
Bracelets $8 for 1, 4 for $20
Toys $15 for 1, $20 for 2 |
Popcorn $5
Cotton Candy $5
CIDER $4

```html
<!DOCTYPE html>
<html lang="en">
<head>
<meta charset="utf-8">
<title>Halloween Price List</title>
<link rel="stylesheet" href="https://fonts.googleapis.com/css2?family=Creepster&family=Permanent+Marker&family=Anton&display=swap">
<style>
  :root {
    --night: #000000;
    --web: #2a2a2a;
    --plum: #55215a;
    --pumpkin: #f7941d;
    --pumpkin-light: #fbb03b;
    --bone: #ffffff;
    --hat: #4a2150;
  }
  * { margin: 0; padding: 0; box-sizing: border-box; }
  html, body { width: 848px; height: 1200px; overflow: hidden; background: var(--night); }
  .poster { position: relative; width: 848px; height: 1200px; background: var(--night); overflow: hidden; }
  .layer { position: absolute; inset: 0; }
  .art { position: absolute; }
  .cobweb { background: radial-gradient(circle, var(--web) 0%, rgba(42,42,42,0) 70%); }
  .pumpkin { border-radius: 50%; background: radial-gradient(circle at 45% 40%, var(--pumpkin-light), var(--pumpkin) 60%, #d35400); }
  .bat, .moon, .icon { background: var(--bone); border-radius: 40%; }

  .headline { position: absolute; white-space: nowrap; line-height: 1; }
  .selling { top: 180px; left: 270px; font-family: "Creepster", cursive; color: var(--pumpkin); font-size: 84px; letter-spacing: 2px; }
  .novelty { top: 298px; left: 132px; font-family: "Permanent Marker", cursive; color: var(--bone); font-size: 62px; }
  .snacks { top: 425px; left: 362px; font-family: "Permanent Marker", cursive; color: var(--bone); font-size: 68px; }

  .banner-text { position: absolute; top: 592px; left: 0; width: 848px; text-align: center; font-family: "Creepster", cursive; font-size: 56px; color: var(--night); letter-spacing: 1px; }

  .item-name { position: absolute; font-family: "Creepster", cursive; color: var(--pumpkin); line-height: 0.95; white-space: nowrap; }
  .item-detail { position: absolute; font-family: "Permanent Marker", cursive; color: var(--bone); font-size: 23px; line-height: 1.45; white-space: nowrap; }
  .price { position: absolute; font-family: "Anton", sans-serif; color: var(--bone); line-height: 1; white-space: nowrap; }

  .bracelets { left: 105px; top: 722px; font-size: 62px; }
  .toys { left: 400px; top: 725px; font-size: 62px; }
  .popcorn { left: 612px; top: 740px; font-size: 46px; }
  .cotton { left: 163px; top: 930px; font-size: 42px; }
  .cider { left: 430px; top: 930px; font-size: 90px; }
</style>
</head>
<body>
<main class="poster">
  <div class="art cobweb" style="left:-80px;top:-60px;width:380px;height:360px" role="img" aria-label="Spider web decoration"></div>
  <div class="art cobweb" style="left:560px;top:-60px;width:380px;height:360px" role="img" aria-label="Spider web decoration"></div>
  <div class="art pumpkin" style="left:50px;top:82px;width:120px;height:95px" role="img" aria-label="Jack-o'-lantern illustration"></div>
  <div class="art pumpkin" style="left:676px;top:82px;width:120px;height:95px" role="img" aria-label="Jack-o'-lantern illustration"></div>

  <svg class="layer" width="848" height="1200" viewBox="0 0 848 1200" aria-hidden="true">
    <path d="M130 120 C220 90 330 110 420 100 C560 85 690 110 735 190 C770 250 720 290 760 350 C800 420 740 490 650 520 C560 550 480 535 410 548 C320 565 230 555 190 500 C150 450 80 440 55 370 C30 300 80 260 70 210 C65 165 90 135 130 120 Z" fill="var(--pumpkin)" transform="translate(6 8)"/>
    <path d="M130 120 C220 90 330 110 420 100 C560 85 690 110 735 190 C770 250 720 290 760 350 C800 420 740 490 650 520 C560 550 480 535 410 548 C320 565 230 555 190 500 C150 450 80 440 55 370 C30 300 80 260 70 210 C65 165 90 135 130 120 Z" fill="var(--plum)"/>
    <path d="M100 600 L745 595 L722 630 L748 668 L140 690 L160 650 Z" fill="var(--bone)"/>
    <line x1="378" y1="722" x2="378" y2="880" stroke="var(--bone)" stroke-width="3"/>
    <line x1="588" y1="718" x2="588" y2="895" stroke="var(--bone)" stroke-width="3"/>
    <line x1="258" y1="800" x2="258" y2="880" stroke="var(--bone)" stroke-width="2"/>
    <line x1="98" y1="908" x2="752" y2="910" stroke="var(--bone)" stroke-width="3"/>
    <line x1="405" y1="935" x2="405" y2="1025" stroke="var(--bone)" stroke-width="3"/>
    <path d="M0 1100 C40 1080 80 1060 120 1085 C150 1110 170 1070 230 1075 C300 1080 330 1110 400 1118 C500 1125 560 1100 620 1080 C680 1060 700 1110 740 1095 C780 1080 800 1060 848 1070 L848 1200 L0 1200 Z" fill="var(--pumpkin)"/>
  </svg>

  <div class="art bat" style="left:425px;top:92px;width:108px;height:34px" role="img" aria-label="Flying bat illustration"></div>
  <div class="art moon" style="left:540px;top:205px;width:38px;height:42px;border-radius:50%" role="img" aria-label="Crescent moon icon"></div>
  <div class="art icon" style="left:598px;top:285px;width:66px;height:95px" role="img" aria-label="Cotton candy illustration"></div>
  <div class="art icon" style="left:212px;top:440px;width:128px;height:70px;background:rgba(255,255,255,0.5)" role="img" aria-label="Charm bracelet illustration"></div>

  <div class="headline selling">SELLING</div>
  <div class="headline novelty">NOVELTY TOYS</div>
  <div class="headline snacks">&amp; SNACKS</div>

  <div class="art bat" style="left:172px;top:607px;width:80px;height:32px;background:var(--night)" role="img" aria-label="Bat silhouette"></div>
  <div class="art bat" style="left:555px;top:605px;width:80px;height:32px;background:var(--night)" role="img" aria-label="Bat silhouette"></div>
  <div class="banner-text">PRICE LIST</div>

  <div class="item-name bracelets">BRACELETS</div>
  <div class="art icon" style="left:80px;top:800px;width:90px;height:58px;background:rgba(255,255,255,0.5)" role="img" aria-label="Charm bracelet illustration"></div>
  <div class="item-detail" style="left:172px;top:795px;text-align:right;width:76px">$8<br>FOR 1,</div>
  <div class="item-detail" style="left:274px;top:795px">4 FOR<br>$20</div>

  <div class="item-name toys">TOYS</div>
  <div class="art icon" style="left:540px;top:765px;width:40px;height:50px;background:var(--pumpkin-light)" role="img" aria-label="Teddy bear and ball illustration"></div>
  <div class="item-detail" style="left:410px;top:818px">$15 FOR 1,<br>$20 FOR 2</div>

  <div class="item-name popcorn">POP<br>CORN</div>
  <div class="art icon" style="left:714px;top:745px;width:38px;height:58px" role="img" aria-label="Popcorn box icon"></div>
  <div class="price" style="left:714px;top:815px;font-size:62px">$5</div>

  <div class="art icon" style="left:110px;top:935px;width:48px;height:78px" role="img" aria-label="Cotton candy icon"></div>
  <div class="item-name cotton">COTTON<br>CANDY</div>
  <div class="price" style="left:282px;top:935px;font-size:92px">$5</div>

  <div class="item-name cider">CIDER</div>
  <div class="art icon" style="left:618px;top:985px;width:18px;height:55px" role="img" aria-label="Cider bottle icon"></div>
  <div class="price" style="left:642px;top:935px;font-size:92px">$4</div>

  <div class="art" style="left:363px;top:1075px;width:120px;height:75px;background:var(--hat);border-radius:40% 40% 20% 20%" role="img" aria-label="Witch hat illustration"></div>
</main>
</body>
</html>
```